Social Media Card

We would like a social media card to hand out to our customers.
It should be double sided, with the front to say in bold letters Follow Us!
We would like the card to be two toned in our brand colors (espresso brown & copper.) I still want a modern, clean look to the card but it can be a bit more "fun" than our business cards. I have attached the previous card that you did but you don't have to stick to the brown background/copper lettering as shown.
The font is josefin. We would need our logo either on the front or the back side.
I think I want social media icons but not the same old boring ones.
Our social media information is as follows:
Facebook: Vandell Jewelry
Twitter: Vandell Jewelry
Pinterest: vkbtqm
Instagram: Vandell Jewelry
Looking forward to seeing what you come up with!
Thanks!
Nell

Our address, etc info will need to be added.

Lakemoor Court # 7

Brookfern Plaza

Londonderry, NH 03999

(603)555-0187

www.vandelljewelry.example

info@vandelljewelry.example

```html
<!DOCTYPE html>
<html lang="en">
<head>
<meta charset="utf-8">
<title>Vandell Jewelry – Social Media Card</title>
<link rel="stylesheet" href="https://fonts.googleapis.com/css2?family=Josefin+Sans:wght@100;300;400&family=Open+Sans:wght@400&display=swap">
<style>
  :root {
    --copper: #c56722;
    --espresso: #2b1910;
    --search-fill: #8c4a1c;
    --search-text: #5a2d10;
    --backdrop: #6d6872;
  }
  * { margin: 0; padding: 0; box-sizing: border-box; }
  html, body { width: 1200px; height: 900px; overflow: hidden; }
  body {
    background: var(--backdrop);
    display: flex;
    align-items: center;
    justify-content: center;
    gap: 60px;
  }
  .card {
    position: relative;
    width: 520px;
    height: 294px;
    background: var(--copper);
    color: var(--espresso);
    font-family: "Josefin Sans", sans-serif;
    overflow: hidden;
  }

  /* Front */
  .front .brand {
    position: absolute;
    left: 0; right: 0; top: 98px;
    text-align: center;
  }
  .brand-name {
    font-weight: 100;
    letter-spacing: 1px;
    line-height: 1;
  }
  .front .brand-name { font-size: 56px; }
  .brand-tagline { font-weight: 300; }
  .front .brand-tagline { font-size: 19px; margin-top: 4px; }
  .follow-pill {
    position: absolute;
    right: 24px; bottom: 24px;
    width: 118px; height: 43px;
    border-radius: 22px;
    background: var(--espresso);
    color: var(--copper);
    font-size: 15px;
    font-weight: 300;
    letter-spacing: 0.5px;
    display: flex; align-items: center; justify-content: center;
    padding-top: 3px;
  }

  /* Back */
  .browser-bar {
    position: absolute;
    left: 0; top: 0; right: 0;
    height: 75px;
    background: var(--espresso);
  }
  .reload-icon { position: absolute; left: 91px; top: 32px; }
  .search-field {
    position: absolute;
    left: 131px; top: 22px;
    width: 373px; height: 43px;
    border-radius: 22px;
    background: var(--search-fill);
    display: flex; align-items: center;
    padding-left: 12px;
    gap: 14px;
  }
  .search-url {
    font-family: "Open Sans", sans-serif;
    font-size: 17px;
    color: var(--search-text);
  }
  .back .brand {
    position: absolute;
    left: 0; right: 0; top: 128px;
    text-align: center;
  }
  .back .brand-name { font-size: 35px; }
  .back .brand-tagline { font-size: 12px; margin-top: 2px; }
  .social-list {
    position: absolute;
    left: 44px; bottom: 28px;
    display: flex;
    list-style: none;
  }
  .social-item {
    display: flex; align-items: center;
    gap: 5px;
    font-family: "Open Sans", sans-serif;
    font-size: 10px;
    margin-right: 12px;
  }
  .social-item:nth-child(1) { width: 116px; }
  .social-item:nth-child(2) { width: 120px; }
  .social-item:nth-child(3) { width: 75px; }
  .social-dot {
    width: 31px; height: 31px;
    border-radius: 50%;
    background: var(--espresso);
    flex: none;
  }
</style>
</head>
<body>
  <section class="card front" aria-label="Card front">
    <div class="brand">
      <div class="brand-name">vandell</div>
      <div class="brand-tagline">Jewelry &amp; Design Studio</div>
    </div>
    <div class="follow-pill">FOLLOW US</div>
  </section>

  <section class="card back" aria-label="Card back">
    <div class="browser-bar">
      <svg class="reload-icon" width="18" height="18" viewBox="0 0 18 18" aria-hidden="true">
        <path d="M14 9a5 5 0 1 1-2-4" fill="none" stroke="#8c4a1c" stroke-width="1.8"/>
        <path d="M10 2.5l3 2.6-3.4 1.6z" fill="#8c4a1c"/>
      </svg>
      <div class="search-field">
        <svg width="26" height="26" viewBox="0 0 26 26" aria-hidden="true">
          <circle cx="15" cy="10" r="7" fill="none" stroke="#2b1910" stroke-width="3"/>
          <path d="M10 15l-7 7" stroke="#2b1910" stroke-width="4" stroke-linecap="round"/>
        </svg>
        <span class="search-url">www.vandelljewelry.example</span>
      </div>
    </div>
    <div class="brand">
      <div class="brand-name">vandell</div>
      <div class="brand-tagline">Jewelry &amp; Design Studio</div>
    </div>
    <ul class="social-list">
      <li class="social-item"><span class="social-dot"></span>Vandell Jewelry</li>
      <li class="social-item"><span class="social-dot"></span>Vandell Jewelry</li>
      <li class="social-item"><span class="social-dot"></span>vkbtqm</li>
      <li class="social-item"><span class="social-dot"></span>Vandell Jewelry</li>
    </ul>
  </section>
</body>
</html>
```